Flyer to Promote Membership in a Trade Association

UPDATE: I am looking for something modern and clean. NO CLIP ART. Not flashy. Just professional and modern. For everyone looking at our current flyer, we don't like it. That's why we aer looking for a new one. So please don't replicate it or use it as inspiration.

I need a flyer to promote membership in the Durable Residence Backers League. It can (probably should) be 2-sided. The content is attached as well as our logo and brand guidelines.

```html
<!DOCTYPE html>
<html lang="en">
<head>
<meta charset="utf-8">
<title>Durable Residence Backers League – Membership Flyer</title>
<link href="https://fonts.googleapis.com/css2?family=Rubik:wght@500;600;700&family=Merriweather:wght@400;700&display=swap" rel="stylesheet">
<style>
  :root{
    --orange:#F4580A;
    --white:#ffffff;
    --stage:#e6e6e6;
    --ink:#4a4f55;
    --head:'Rubik', Arial, sans-serif;
    --body:'Merriweather', Georgia, serif;
  }
  *{margin:0;padding:0;box-sizing:border-box}
  html,body{width:1200px;height:900px;overflow:hidden;background:var(--stage)}
  .flyer{position:absolute;left:157px;top:137px;width:887px;height:626px;background:var(--white);overflow:hidden}
  .bands{position:absolute;inset:0}
  .abs{position:absolute}
  .brand{left:13px;top:12px;display:flex;align-items:center;gap:8px;font:700 29px/1 var(--head);color:var(--white)}
  .brand-square{width:24px;height:24px;background:var(--white)}
  .brand-name{left:7px;top:62px;font:700 7.4px/1 var(--body);color:var(--orange)}
  .headline{left:18px;top:93px;font:600 18px/20.4px var(--head);color:var(--orange)}
  .headline mark{background:var(--orange);color:var(--white);padding:0 3px}
  .intro{left:18px;top:169px;width:420px;font:700 8px/10.5px var(--body);color:var(--ink)}
  .stat-box{width:44px;height:44px;background:var(--white);color:var(--orange);font:700 26px/44px var(--head);text-align:center}
  .stat-box.small{font-size:21px}
  .stat-label{font:600 16px/1 var(--head);color:var(--white)}
  .big-num{left:250px;top:258px;font:700 56px/1 var(--head);color:var(--white)}
  .big-label{left:251px;top:314px;font:600 20px/22px var(--head);color:var(--white)}
  .section-title{font:600 13.5px/1 var(--head);color:var(--orange)}
  .do-list{font:400 9.6px/14.5px var(--body);color:var(--ink);list-style:none}
  .callout{left:0;width:443px;text-align:center;font:600 10px/12.5px var(--head);color:var(--orange)}
  .tier{left:52px;font:400 9.4px/11.5px var(--body);color:var(--ink)}
  .price{left:218px;width:173px;height:38px;background:var(--orange);color:var(--white);display:flex;flex-direction:column;justify-content:center;align-items:center;font:500 11.6px/16px var(--head)}
  .price.flat{font:600 22px/1 var(--head)}
  .benefits-title{left:443px;width:443px;top:68px;text-align:center;font:600 17px/1 var(--head);color:var(--orange)}
  .benefit{left:476px;width:380px}
  .benefit h3{font:500 13.6px/1 var(--head);color:var(--orange);margin-bottom:5px}
  .benefit p{font:400 7.4px/10px var(--body);color:#333}
  .members{left:476px;top:442px;width:380px;font:400 7.5px/10.9px var(--body);color:#333}
  .cta{left:476px;top:522px;font:600 12px/1 var(--head);color:var(--orange)}
</style>
</head>
<body>
<div class="flyer">
  <svg class="bands" viewBox="261 228 1478 1044" width="887" height="626" aria-hidden="true">
    <polygon fill="#F4580A" points="261,228 730,228 750,258 1739,258 1739,313 1000,313 1000,350 530,350 510,320 261,320"/>
    <polygon fill="#F4580A" points="261,599 730,599 750,629 1000,629 1000,867 620,867 603,838 261,838"/>
    <polygon fill="#F4580A" points="1000,1151 1470,1151 1488,1180 1739,1180 1739,1272 1268,1272 1250,1243 1000,1243"/>
  </svg>

  <div class="abs brand"><span class="brand-square"></span>DRBL</div>
  <div class="abs brand-name">Durable Residence Backers League</div>

  <h1 class="abs headline">Where LIHTC Investing Excellence Begins<br>The Only Community Built Exclusively<br>for <mark>Investors</mark></h1>

  <p class="abs intro">DRBL is where federal housing credit investors connect, learn, and lead.<br>We are the only organization solely dedicated to LIHTC investors—giving you a trusted peer network, industry-setting standards, and the insights to stay informed.</p>

  <div class="abs stat-box" style="left:31px;top:242px">30</div>
  <div class="abs stat-label" style="left:88px;top:256px">YEARS OF IMPACT</div>
  <div class="abs stat-box small" style="left:31px;top:301px">60+</div>
  <div class="abs stat-label" style="left:87px;top:316px">INVESTOR FIRMS</div>
  <div class="abs big-num">1000+</div>
  <div class="abs big-label">INDUSTRY<br>PROFESSIONALS</div>

  <h2 class="abs section-title" style="left:41px;top:383px">WHAT MEMBERS DO</h2>
  <ul class="abs do-list" style="left:41px;top:406px">
    <li>Network: Peer Groups &amp; Forums</li>
    <li>Learn: Conferences &amp; Webinars</li>
    <li>Share: Candid Investor Exchange</li>
  </ul>
  <ul class="abs do-list" style="left:240px;top:406px">
    <li>Shape: Standards &amp; Best Practices</li>
    <li>Grow: Professional Development</li>
  </ul>

  <p class="abs callout" style="top:463px">One membership, unlimited access.<br>Your entire team can participate in DRBL activities.</p>
  <h2 class="abs section-title callout" style="top:499px;font-size:13.5px">JOIN DRBL TODAY</h2>

  <p class="abs tier" style="top:527px">Investor Members<br>Banks, Insurance Companies,<br>Economic Investors</p>
  <div class="abs price" style="top:523px"><span>$5,000/year (assets ≥$5B)</span><span>$1,000/year (assets &lt;$5B)</span></div>
  <p class="abs tier" style="top:576px">Affiliate Member<br>Syndicators &amp; Brokers</p>
  <div class="abs price flat" style="top:568px">$4,500/year</div>

  <h2 class="abs benefits-title">MEMBER BENEFITS</h2>

  <div class="abs benefit" style="top:108px"><h3>MEMBERS-ONLY CONFERENCES</h3><p>Two annual in-person meetings. Spring Meeting: investors-only for candid peer conversations.<br>Fall Summit: full ecosystem gathering with syndicators and brokers.</p></div>
  <div class="abs benefit" style="top:154px"><h3>INVESTOR-ONLY FORUMS</h3><p>Exclusive meetings and webinars for investors only, enabling candid conversations and meaningful collaboration.</p></div>
  <div class="abs benefit" style="top:200px"><h3>PEER-TO-PEER MEETUPS</h3><p>Find your peers—underwriters, asset managers, credit officers and more—with our meetups.</p></div>
  <div class="abs benefit" style="top:237px"><h3>LIVE &amp; ON-DEMAND WEBINARS</h3><p>Free monthly Third Thursday webinars covering Year 15 issues, secondary transactions,<br>securitizing developer fees and other emerging topics.</p></div>
  <div class="abs benefit" style="top:285px"><h3>SEARCHABLE MEMBER DIRECTORY</h3><p>Find underwriters, asset managers, and credit officers—searchable by role, firm type,<br>and investment approach.</p></div>
  <div class="abs benefit" style="top:332px"><h3>SHAPE INDUSTRY STANDARDS&nbsp; [INVESTOR ONLY]</h3><p>DRBL's underwriting and asset management standards are adopted industry-wide.<br>Influence them through our committees.</p></div>
  <div class="abs benefit" style="top:389px;width:400px"><h3>EMERGING LEADERS PROGRAM&nbsp; [INVESTOR ONLY]</h3><p>Develop your firm's next-generation leaders through dedicated professional development programming.</p></div>

  <p class="abs members">Our Investor Members Include<br>Orlenna Life Group&nbsp; Pellwick Bank&nbsp; Thessaly Crest National Bank&nbsp; Bank of Orvane&nbsp; Dunmarrow Bank&nbsp; Halvern Financial&nbsp; Corvessa Capital&nbsp; Ashwend Trust Bank&nbsp; Brennick Trust&nbsp; Lowmere CDC&nbsp; Quarrystone Bank&nbsp; Veltrane Partners&nbsp; Tallowby Bank&nbsp; Quillfield Capital&nbsp; Sablecroft Insurance&nbsp; Embervale Life&nbsp; Corlith Investors&nbsp; Wrenhollow Real Estate&nbsp; Larchmere Housing Capital&nbsp; Ostwick Bank&nbsp; Palvane Coatings&nbsp; Saltmarsh Bank&nbsp; Glenharrow Bank&nbsp; Brightfen Community Capital&nbsp; Kestrow Bank&nbsp; Copperline Mutual&nbsp; Ravensholm Impact Finance&nbsp; Thornacre Bank</p>

  <p class="abs cta">Ready to join?&nbsp; drbl.org</p>
</div>
</body>
</html>
```